Namecard Designs+Logo for a High End Automobile Company

We need a new business card for our company called Velta Motorhof.

www.veltamotorhof.example.sg
Our new website will be up in 2.5 months time.

We sell used and brand new continental cars like Stavaro, KTJ, Lindqvar, Castrelli and etc. Currently we are operating from 2 offices in Singapore and United Kingdom.

We want a design which is serious. We are open to colours but try to keep it at a maximum of 3 colours.

We prefer something simple and minimal. We are open to 2 sides printing or even 2 sided namecards. Both UK and Singapore company offices address must be in; either side by side, front and back, or even 2 sided cards.

The logo can be a text logo, emblem, abstract, pictorial or combination.

We are printing with Prinvo.example so please kindly follow the printing guideline.

http://uk.prinvo.example/help/faq/templates-and-guidelines.html

Target Market(s)

Rich and Car Enthusiasts

Industry/Entity Type

Printing

Requirements
Must have
• Our 2 offices; UK and Singapore.

Our slogan which is " The Automobile Specialist"
Should not have
• Not more than 3 colours

```html
<!DOCTYPE html>
<html lang="en">
<head>
<meta charset="utf-8">
<title>Velta Motorhof – Business Cards</title>
<link rel="stylesheet" href="https://fonts.googleapis.com/css2?family=Questrial&display=swap">
<style>
  :root {
    --backdrop: #bbbcbe;
    --ink: #1b1a1a;
    --card-dark: #1f1e1e;
    --card-gloss: #3a3a3b;
    --card-light: #ffffff;
    --paper-text: #ffffff;
    --logo-grey: #9a9a9c;
  }
  * { margin: 0; padding: 0; box-sizing: border-box; }
  html, body { width: 1200px; height: 900px; overflow: hidden; }
  body {
    background: var(--backdrop);
    font-family: "Questrial", "Century Gothic", sans-serif;
    position: relative;
  }
  .card {
    position: absolute;
    width: 518px;
    height: 309px;
    border-radius: 36px;
    overflow: hidden;
  }
  .card--uk { left: 82px; top: 79px; background: var(--card-dark); color: var(--paper-text); }
  .card--sg { left: 622px; top: 363px; background: var(--card-light); color: var(--ink); }
  .card__art { position: absolute; inset: 0; width: 100%; height: 100%; }
  .contact {
    position: absolute;
    left: 61px;
    top: 32px;
    font-size: 13px;
    line-height: 20px;
    list-style: none;
  }
  .contact__name { font-size: 16px; font-weight: 700; letter-spacing: 0.2px; }
  .card-logo {
    position: absolute;
    right: 16px;
    top: 246px;
    text-align: right;
  }
  .card-logo__name {
    display: block;
    font-size: 21px;
    letter-spacing: 1.2px;
    line-height: 1;
  }
  .card--uk .card-logo__name { color: var(--logo-grey); }
  .card-logo__slogan { display: block; font-size: 9px; margin-top: 4px; margin-right: 8px; }
  .brand-mark {
    position: absolute;
    left: 168px;
    top: 728px;
    width: 940px;
    color: var(--ink);
    text-align: right;
  }
  .brand-mark__name {
    display: block;
    font-size: 66px;
    letter-spacing: 9px;
    line-height: 1;
    white-space: nowrap;
  }
  .brand-mark__slogan { display: block; font-size: 34px; margin-top: 14px; }
</style>
</head>
<body>

  <section class="card card--uk" aria-label="United Kingdom office card">
    <svg class="card__art" viewBox="0 0 518 309" aria-hidden="true">
      <defs>
        <linearGradient id="gloss" x1="0" y1="0" x2="1" y2="1">
          <stop offset="0" stop-color="#4a4a4b"/>
          <stop offset="0.6" stop-color="#2a2a2b"/>
        </linearGradient>
      </defs>
      <path d="M0 250 C60 110 250 25 518 15 L518 0 L0 0 Z" fill="url(#gloss)"/>
      <path d="M0 242 C150 225 260 150 400 150 C460 150 500 158 518 162 L518 170 C480 162 450 157 400 158 C280 160 160 235 0 248 Z" fill="#ffffff"/>
    </svg>
    <ul class="contact">
      <li class="contact__name">Rhys Palmer</li>
      <li>1-800-555-0148</li>
      <li>48 Harrow Lane</li>
      <li>London</li>
      <li>W1X 2QP</li>
      <li>www.veltamotorhof.example.uk</li>
    </ul>
    <div class="card-logo">
      <span class="card-logo__name">VELTA MOTORHOF</span>
      <span class="card-logo__slogan">The Automobile Specialist</span>
    </div>
  </section>

  <section class="card card--sg" aria-label="Singapore office card">
    <svg class="card__art" viewBox="0 0 518 309" aria-hidden="true">
      <path d="M0 244 C150 228 260 150 400 150 C460 150 500 154 518 158 L518 166 C480 158 450 155 400 156 C280 160 160 236 0 248 Z" fill="#1b1a1a"/>
    </svg>
    <ul class="contact">
      <li class="contact__name">Rhys Palmer</li>
      <li>1-800-555-0148</li>
      <li>17 Keppel Rise</li>
      <li>#03-12 Orin Tech Centre</li>
      <li>Singapore</li>
      <li>www.veltamotorhof.example.sg</li>
    </ul>
    <div class="card-logo">
      <span class="card-logo__name">VELTA MOTORHOF</span>
      <span class="card-logo__slogan">The Automobile Specialist</span>
    </div>
  </section>

  <div class="brand-mark">
    <span class="brand-mark__name">VELTA MOTORHOF</span>
    <span class="brand-mark__slogan">The Automobile Specialist</span>
  </div>

</body>
</html>
```